Simple proffessional BC

I have a logo which I will attach below.
I would like the logo on the front of the card with these details in point form below:
Pre and Post Natal Yoga: Pregnancy Workshops: Hypnobirthing Courses
On the back of the card my details:
Marla Penrick
Pagebook page- calmcradlestudiolakebay
Mobile- 0482 315 746

I like the idea of the card being simple, possibly just the above on a plain coloured (eggshell?) card, a card that is textured.
I am open to suggestion if it appeals!
Thank you and good luck!

Target Market(s)

Pregnant women, 20's-40's

Requirements
Must have
• Simple, compliment logo.
Make logo the feature.
Should not have

```html
<!DOCTYPE html>
<html lang="en">
<head>
<meta charset="utf-8">
<title>Calm Cradle – Business Card</title>
<link href="https://fonts.googleapis.com/css2?family=Questrial&display=swap" rel="stylesheet">
<style>
  :root {
    --maroon: #5e1312;
    --maroon-deep: #4d0f0e;
    --saffron: #e9a23b;
    --eggshell: #fbecd9;
    --eggshell-shade: #f3e0c8;
    --backdrop: #2e2e2e;
  }
  * { margin: 0; padding: 0; box-sizing: border-box; }
  html, body {
    width: 1200px; height: 900px; overflow: hidden;
    background: var(--backdrop);
    font-family: "Questrial", "Century Gothic", sans-serif;
  }
  .sheet {
    width: 1200px; height: 900px;
    display: flex; flex-direction: column; align-items: center; justify-content: center;
    gap: 40px;
  }
  .card {
    position: relative;
    width: 700px; height: 400px;
    overflow: hidden;
    box-shadow: 0 10px 30px rgba(0,0,0,.45);
  }

  /* Front */
  .card-front { background: var(--maroon); }
  .front-mark {
    position: absolute; left: 50%; top: 42px; transform: translateX(-50%);
    display: flex; flex-direction: column; align-items: center; gap: 14px;
  }
  .front-mark .disc {
    width: 190px; height: 190px; border-radius: 50%; background: var(--saffron);
  }
  .front-mark .brand {
    color: var(--saffron); font-size: 30px; letter-spacing: 1px;
  }
  .services {
    position: absolute; right: 34px; bottom: 30px;
    color: var(--saffron); font-size: 15px; letter-spacing: .4px;
  }
  .services .sep { margin: 0 8px; }

  /* Back */
  .card-back { background: var(--eggshell); }
  .card-back::after {
    content: ""; position: absolute; left: 0; right: 0; bottom: 0; height: 10px;
    background: var(--maroon);
  }
  .back-halo {
    position: absolute; right: 40px; top: 30px;
    width: 300px; height: 300px; border-radius: 50%;
    background: var(--eggshell-shade); opacity: .7;
  }
  .back-brand {
    position: absolute; left: 60px; top: 60px;
    display: flex; align-items: center; gap: 22px;
  }
  .back-brand .disc {
    width: 110px; height: 110px; border-radius: 50%; background: var(--saffron);
  }
  .back-brand .brand { color: var(--maroon); font-size: 52px; }
  .holder {
    position: absolute; left: 300px; top: 190px;
    color: var(--maroon); font-size: 36px; letter-spacing: .5px;
  }
  .phone {
    position: absolute; left: 300px; top: 255px;
    display: flex; align-items: center; gap: 10px;
    color: var(--maroon); font-size: 26px; letter-spacing: 1px;
  }
  .phone .icon {
    width: 32px; height: 32px; border-radius: 50%; background: var(--saffron);
    display: flex; align-items: center; justify-content: center;
  }
  .social {
    position: absolute; left: 40px; bottom: 34px;
    display: flex; align-items: flex-end; gap: 6px; color: var(--maroon);
  }
  .social .network { display: flex; flex-direction: column; line-height: 1; }
  .social .invite { font-size: 9px; letter-spacing: 1px; margin-bottom: 3px; }
  .social .network-name { font-size: 22px; }
  .social .handle { font-size: 26px; letter-spacing: .5px; line-height: 1; }
</style>
</head>
<body>
<main class="sheet">
  <section class="card card-front">
    <div class="front-mark">
      <div class="disc"></div>
      <span class="brand">Calm Cradle</span>
    </div>
    <p class="services">Pre and Post Natal Yoga<span class="sep">|</span>Pregnancy Workshops<span class="sep">|</span>Hypnobirthing Courses</p>
  </section>

  <section class="card card-back">
    <div class="back-halo"></div>
    <div class="back-brand">
      <div class="disc"></div>
      <span class="brand">Calm Cradle</span>
    </div>
    <p class="holder">Marla Penrick</p>
    <p class="phone">
      <span class="icon">
        <svg width="14" height="20" viewBox="0 0 14 20" aria-hidden="true">
          <rect x="1" y="1" width="12" height="18" rx="2" fill="none" stroke="#5e1312" stroke-width="1.8"/>
          <rect x="3.5" y="3.5" width="7" height="11" fill="#5e1312"/>
          <circle cx="7" cy="16.6" r="1" fill="#5e1312"/>
        </svg>
      </span>
      0482 315 746
    </p>
    <div class="social">
      <div class="network">
        <span class="invite">LIKE US ON</span>
        <span class="network-name">Pagebook</span>
      </div>
      <span class="handle">/calmcradlestudiolakebay</span>
    </div>
  </section>
</main>
</body>
</html>
```